Web design project for exciting Australian start-up

Background
We are looking for a creative and talented web design artist to work alongside our market leading web developer.
• You will be required to create a modern and clean design theme for our website, incorporating selected rustic colour scheme elements for our exciting Australian start-up to operate within the coffee industry.
reoccurring work to be expected to flow to the successful designer.
Requirements
• c. 5 - 10 page website
• Landing page
• Log in/ out
• 404 template
• Typography is emphasised
• Please use either a) quillnest.com, b) free web fonts, c) plovra fonts
• All design elements in vector format
• Preferably with icons for each header title(i.e. about us, how it works etc) but designer have free reign over how the site looks, so might not be applicable
• All pages to be responsive
• Down to Kelvo resolution

High level visual design brief attached - additional pages to be worked from base design.

Design inspiration
• We would like to use design elements from the following sources:
http://www.plovra.com/vintel/ (Functionality)
Colour scheme refer to logo and complementary style guide

```html
<!DOCTYPE html>
<html lang="en">
<head>
<meta charset="utf-8">
<title>Brewhaven – Coffee Marketplace</title>
<link rel="stylesheet" href="https://fonts.googleapis.com/css2?family=Lato:wght@400;700;900&family=Open+Sans:wght@300;700&family=Roboto+Slab:wght@300;400&display=swap">
<style>
  :root {
    --orange: #fea032;
    --red: #ee3d3f;
    --ink: #333333;
    --muted: #555555;
    --nav-active: #f4f4f4;
    --rule: #ebebeb;
    --footer-bg: #e7e7e7;
    --base-bg: #535353;
    --base-rule: #6c6c6c;
    --white: #ffffff;
  }
  * { box-sizing: border-box; margin: 0; padding: 0; }
  html, body { width: 1200px; height: 950px; overflow: hidden; background: var(--white); }
  body { position: relative; font-family: "Lato", sans-serif; color: var(--ink); }

  .site-header { position: absolute; left: 0; top: 0; width: 1200px; height: 107px; background: var(--white); }
  .brand { position: absolute; left: 161px; top: 33px; display: flex; align-items: center; gap: 10px; }
  .brand-mark { width: 40px; height: 40px; border-radius: 50%; background: var(--orange); }
  .brand-name { font-family: "Lato", sans-serif; font-weight: 900; font-size: 27px; letter-spacing: 2px; color: #1e1e1e; }

  .main-nav { position: absolute; top: 0; left: 560px; height: 107px; display: flex; border-left: 1px solid var(--rule); }
  .nav-item { height: 107px; display: flex; flex-direction: column; align-items: center; justify-content: center; gap: 8px;
    border-right: 1px solid var(--rule); font-size: 12px; text-transform: uppercase; color: var(--ink); text-decoration: none; }
  .nav-item svg { width: 20px; height: 20px; }
  .nav-item.is-active { background: var(--nav-active); }
  .nav-about { width: 94px; }
  .nav-how { width: 135px; }
  .nav-faq { width: 66px; }

  .auth { position: absolute; top: 38px; left: 878px; display: flex; gap: 10px; }
  .btn { height: 31px; width: 75px; display: flex; align-items: center; justify-content: center; color: var(--white);
    font-size: 14px; border-radius: 2px; text-decoration: none; }
  .btn-login { background: var(--orange); }
  .btn-signup { background: var(--red); }

  .hero { position: absolute; left: 0; top: 107px; width: 1200px; height: 543px; overflow: hidden; }
  .hero-photo { position: absolute; inset: 0;
    background: radial-gradient(ellipse 520px 300px at 600px 360px, #d9cbbd 0%, #bba693 45%, transparent 75%),
                linear-gradient(135deg, #9f8d86 0%, #a8968c 40%, #8f7d75 70%, #5f5550 100%); }
  .hero-copy { position: absolute; left: 0; right: 0; top: 212px; text-align: center; color: var(--white); font-family: "Open Sans", sans-serif; }
  .hero-kicker { font-weight: 300; font-size: 22px; letter-spacing: 0.5px; line-height: 1; }
  .hero-title { margin-top: 10px; font-weight: 700; font-size: 37px; line-height: 1; letter-spacing: 0.5px; }
  .hero-cta { position: absolute; left: 519px; top: 302px; width: 162px; height: 45px; background: var(--orange); color: var(--white);
    font-family: "Lato", sans-serif; font-size: 17px; display: flex; align-items: center; justify-content: center; text-decoration: none; }
  .slider-arrow { position: absolute; top: 240px; width: 56px; height: 56px; border: 2px solid var(--white); border-radius: 50%;
    display: flex; align-items: center; justify-content: center; }
  .slider-arrow svg { width: 14px; height: 14px; }
  .slider-prev { left: 161px; }
  .slider-next { left: 982px; }

  .site-footer { position: absolute; left: 0; top: 650px; width: 1200px; height: 236px; background: var(--footer-bg); }
  .footer-col { position: absolute; top: 51px; }
  .footer-col h3 { font-family: "Roboto Slab", serif; font-weight: 400; font-size: 18px; color: #222; letter-spacing: 0.3px; }
  .footer-col ul { list-style: none; margin-top: 16px; }
  .footer-col li { font-family: "Roboto Slab", serif; font-weight: 300; font-size: 14px; color: var(--muted); height: 31px; display: flex; align-items: center; }
  .col-info { left: 295px; }
  .col-who { left: 541px; }
  .col-who ul, .col-join ul { padding-left: 3px; }
  .col-join { left: 797px; }
  .social-label { width: 76px; }
  .social-dot { width: 10px; height: 10px; border-radius: 50%; background: var(--muted); }

  .base-bar { position: absolute; left: 0; top: 886px; width: 1200px; height: 64px; background: var(--base-bg); }
  .base-bar .rule { position: absolute; left: 161px; top: 5px; width: 877px; height: 1px; background: var(--base-rule); }
  .copyright { position: absolute; left: 0; right: 0; top: 24px; text-align: center; color: var(--white); font-size: 14px; }
</style>
</head>
<body>
  <header class="site-header">
    <div class="brand">
      <span class="brand-mark"></span>
      <span class="brand-name">BREWHAVEN</span>
    </div>
    <nav class="main-nav">
      <a class="nav-item nav-about is-active" href="#">
        <svg viewBox="0 0 20 20" fill="none" stroke="#fea032" stroke-width="1.3"><path d="M3 10 L10 3 L17 10"/><path d="M5 8.5 V17 H15 V8.5"/><rect x="8.5" y="12" width="3" height="5"/></svg>
        About Us
      </a>
      <a class="nav-item nav-how" href="#">
        <svg viewBox="0 0 20 20" fill="none" stroke="#777" stroke-width="1.3"><circle cx="8" cy="7" r="3"/><path d="M2 18 C2 13 14 13 14 18"/><rect x="12" y="2" width="6" height="5"/></svg>
        How It Works
      </a>
      <a class="nav-item nav-faq" href="#">
        <svg viewBox="0 0 20 20" fill="none" stroke="#777" stroke-width="1.3"><rect x="4" y="4" width="3" height="14"/><rect x="9" y="6" width="3" height="12"/><rect x="14" y="2" width="3" height="16"/></svg>
        FAQ
      </a>
    </nav>
    <div class="auth">
      <a class="btn btn-login" href="#">Login</a>
      <a class="btn btn-signup" href="#">Sign up</a>
    </div>
  </header>

  <section class="hero">
    <div class="hero-photo" role="img" aria-label="Cappuccino with cinnamon-dusted foam and a cinnamon stick on a map backdrop"></div>
    <a class="slider-arrow slider-prev" href="#" aria-label="Previous slide">
      <svg viewBox="0 0 14 14" fill="none" stroke="#fff" stroke-width="2"><path d="M9 2 L4 7 L9 12"/></svg>
    </a>
    <div class="hero-copy">
      <p class="hero-kicker">AUSTRALIA FIRST ONLINE</p>
      <h1 class="hero-title">COFFEE MARKETPLACE</h1>
    </div>
    <a class="hero-cta" href="#">Watch Video</a>
    <a class="slider-arrow slider-next" href="#" aria-label="Next slide">
      <svg viewBox="0 0 14 14" fill="none" stroke="#fff" stroke-width="2"><path d="M5 2 L10 7 L5 12"/></svg>
    </a>
  </section>

  <footer class="site-footer">
    <div class="footer-col col-info">
      <h3>HELPFUL INFO</h3>
      <ul>
        <li>About Us</li>
        <li>Media Enquiries</li>
        <li>Terms &amp; Conditions</li>
        <li>Privacy Policy</li>
      </ul>
    </div>
    <div class="footer-col col-who">
      <h3>WHO WE ARE</h3>
      <ul>
        <li>How it works</li>
        <li>FAQ</li>
        <li>Contact us</li>
      </ul>
    </div>
    <div class="footer-col col-join">
      <h3>JOIN US ON</h3>
      <ul>
        <li><span class="social-label">Friendwall</span><span class="social-dot"></span></li>
        <li><span class="social-label">Chirper</span><span class="social-dot"></span></li>
        <li><span class="social-label">Workweb</span><span class="social-dot"></span></li>
        <li><span class="social-label">Vidstream</span><span class="social-dot"></span></li>
      </ul>
    </div>
  </footer>

  <div class="base-bar">
    <div class="rule"></div>
    <p class="copyright">Copyright © 2014 Brewhaven</p>
  </div>
</body>
</html>
```